Flyer Template

I need a flyer template for door knocking on properties. Text Boxes need to be editable, with a header and text body. Footer to be my info. Project to be stylized to match my real estate signs and logo art from past projects

```html
<!DOCTYPE html>
<html lang="en">
<head>
<meta charset="UTF-8">
<title>Elegant Home For Sale – Flyer</title>
<link href="https://fonts.googleapis.com/css2?family=Bebas+Neue&family=Montserrat:wght@400;500;600;700&family=Tangerine:wght@700&display=swap" rel="stylesheet">
<style>
  :root {
    --red: #f70f1a;
    --ink: #111111;
    --dark-red-text: #2a0506;
    --paper: #ffffff;
    --mist: #eeeff2;
    --backdrop: #f2f2f2;
    --footer-black: #0b0b0b;
  }
  * { margin: 0; padding: 0; box-sizing: border-box; }
  html, body { width: 800px; height: 1200px; overflow: hidden; background: var(--backdrop); }
  body { font-family: "Montserrat", Arial, sans-serif; color: var(--ink); position: relative; }

  .flyer {
    position: absolute; left: 0; top: 33px;
    width: 811px; height: 1150px;
    background: var(--paper);
    transform: scale(0.9865); transform-origin: 0 0;
    overflow: hidden;
  }
  .layer { position: absolute; left: 0; top: 0; }

  /* brand */
  .brand { position: absolute; left: 36px; top: 60px; width: 130px; text-align: center; }
  .brand-mark { display: block; width: 30px; height: 30px; background: var(--red); margin: 0 auto 12px; }
  .brand-name { font-weight: 700; font-size: 19px; line-height: 26px; letter-spacing: 0.5px; color: var(--ink); }

  /* hero text */
  .hero { position: absolute; left: 36px; top: 200px; width: 340px; color: var(--paper); }
  .hero-script { font-family: "Tangerine", cursive; font-weight: 700; font-size: 92px; line-height: 80px; color: var(--ink); white-space: nowrap; max-width: 340px; }
  .hero-title { font-family: "Bebas Neue", sans-serif; font-size: 104px; line-height: 86px; margin-top: -2px; letter-spacing: 0.5px; }
  .hero-rule { width: 256px; height: 1px; background: rgba(255,255,255,0.85); margin-top: 26px; }
  .price-label { font-size: 23px; font-weight: 400; color: var(--dark-red-text); margin-top: 25px; letter-spacing: -0.2px; }
  .price-value { font-family: "Bebas Neue", sans-serif; font-size: 66px; line-height: 62px; margin-top: 4px; }
  .price-value sup { font-size: 26px; vertical-align: 26px; margin-right: 1px; }

  /* info section */
  .section-heading { font-size: 21px; font-weight: 600; letter-spacing: 0.4px; color: var(--ink); }
  .section-heading .accent { color: var(--red); }
  .about { position: absolute; left: 40px; top: 610px; width: 350px; }
  .about-body { font-size: 15.3px; line-height: 18.6px; margin-top: 10px; letter-spacing: 0.1px; }
  .features { position: absolute; left: 424px; top: 610px; width: 370px; }
  .feature-cols { display: flex; margin-top: 10px; }
  .feature-list { list-style: none; }
  .feature-list li { display: flex; align-items: center; font-size: 15.3px; height: 29px; letter-spacing: 0.2px; }
  .feature-list li svg { width: 15px; height: 15px; margin-right: 10px; flex: none; }
  .feature-list.first { width: 175px; padding-left: 2px; }
  .feature-list.second { border-left: 1px solid #c9cacd; padding-left: 20px; }

  /* gallery */
  .gallery { position: absolute; left: 38px; top: 805px; display: flex; gap: 20px; }
  .gallery-frame { width: 228px; height: 190px; background: var(--paper); padding: 6px; box-shadow: 0 1px 5px rgba(0,0,0,0.18); }
  .gallery-photo { width: 100%; height: 100%; }
  .photo-modern { background: linear-gradient(180deg, #c9ced3 0%, #3c3d40 35%, #2a2a2c 70%, #5a6b3c 100%); }
  .photo-blue { background: linear-gradient(180deg, #6c86b8 0%, #3d4f7c 35%, #34456e 65%, #4d8a2a 100%); }
  .photo-evening { background: linear-gradient(180deg, #5b73c2 0%, #8ea2d8 40%, #6d6f7c 65%, #b89a72 100%); }

  /* tagline */
  .tagline { position: absolute; left: 40px; top: 1022px; font-size: 17px; font-weight: 700; line-height: 21px; letter-spacing: 0.2px; }
  .tagline .accent { color: var(--red); display: block; }
  .tagline-body { position: absolute; left: 260px; top: 1022px; width: 530px; font-size: 15.2px; line-height: 19px; letter-spacing: 0.1px; }

  /* footer */
  .contact-call { position: absolute; left: 40px; top: 1092px; color: var(--paper); }
  .call-label { font-size: 13.5px; }
  .call-number { display: flex; align-items: center; color: var(--red); font-weight: 700; font-size: 21px; letter-spacing: 0.3px; margin-top: 1px; }
  .call-number svg { width: 17px; height: 17px; margin-right: 7px; }
  .contact-details { position: absolute; left: 274px; top: 1100px; display: flex; align-items: flex-start; color: var(--paper); font-size: 9.4px; line-height: 11.5px; }
  .contact-item { display: flex; align-items: flex-start; }
  .contact-item svg { width: 10px; height: 10px; margin-right: 6px; margin-top: 1px; flex: none; }
  .contact-sep { width: 1px; height: 16px; background: rgba(255,255,255,0.8); margin: 0 8px; }
</style>
</head>
<body>
<main class="flyer">
  <svg class="layer" width="811" height="1150" viewBox="0 0 811 1150" aria-hidden="true">
    <defs>
      <linearGradient id="heroHouse" x1="0" y1="0" x2="0" y2="1">
        <stop offset="0" stop-color="#6e92c8"/>
        <stop offset="0.3" stop-color="#5e6a86"/>
        <stop offset="0.55" stop-color="#8b8682"/>
        <stop offset="0.75" stop-color="#5f7a3a"/>
        <stop offset="1" stop-color="#3f7a22"/>
      </linearGradient>
    </defs>
    <rect class="mist-band" x="0" y="480" width="811" height="295" fill="#eeeff2"/>
    <polygon points="271,0 811,0 811,595 392,505 392,110 271,135" fill="url(#heroHouse)"/>
    <polygon points="0,188 392,104 392,505 0,590" fill="#ffffff"/>
    <polygon points="0,197 392,114 392,505 0,585" fill="#f70f1a"/>
    <polygon points="0,1080 242,1080 262,1150 0,1150" fill="#0b0b0b"/>
    <polygon points="248,1080 811,1080 811,1150 268,1150" fill="#f70f1a"/>
  </svg>
  <div class="layer" role="img" aria-label="Photograph of a two-storey craftsman house with lit porch and green lawn" style="left:392px;top:0;width:419px;height:500px;"></div>

  <div class="brand">
    <span class="brand-mark"></span>
    <div class="brand-name">MARLOWE<br>REALTY</div>
  </div>

  <section class="hero">
    <div class="hero-script">Elegant Home</div>
    <h1 class="hero-title">FOR SALE</h1>
    <div class="hero-rule"></div>
    <p class="price-label">PRICE STARTS FROM</p>
    <p class="price-value"><sup>$</sup>2,150,000</p>
  </section>

  <section class="about">
    <h2 class="section-heading">ABOUT THE <span class="accent">PROPERTY</span></h2>
    <p class="about-body">Lorem Ipsum is simply dummy text of the printing and typesetting industry. Lorem Ipsum has been the industry's standard dummy text ever since the 1500s, when an unknown printer took a galley of type and scrambled it to make a type specimen book.</p>
  </section>

  <section class="features">
    <h2 class="section-heading">PROPERTY <span class="accent">FEATURE</span></h2>
    <div class="feature-cols">
      <ul class="feature-list first">
        <li><svg viewBox="0 0 16 16"><circle cx="8" cy="8" r="8" fill="#f70f1a"/><path d="M4.5 8.2l2.3 2.3 4.7-4.8" stroke="#fff" stroke-width="2" fill="none"/></svg>Living Room</li>
        <li><svg viewBox="0 0 16 16"><circle cx="8" cy="8" r="8" fill="#f70f1a"/><path d="M4.5 8.2l2.3 2.3 4.7-4.8" stroke="#fff" stroke-width="2" fill="none"/></svg>Dining Room</li>
        <li><svg viewBox="0 0 16 16"><circle cx="8" cy="8" r="8" fill="#f70f1a"/><path d="M4.5 8.2l2.3 2.3 4.7-4.8" stroke="#fff" stroke-width="2" fill="none"/></svg>Swimming Room</li>
        <li><svg viewBox="0 0 16 16"><circle cx="8" cy="8" r="8" fill="#f70f1a"/><path d="M4.5 8.2l2.3 2.3 4.7-4.8" stroke="#fff" stroke-width="2" fill="none"/></svg>2 Kitchens</li>
      </ul>
      <ul class="feature-list second">
        <li><svg viewBox="0 0 16 16"><circle cx="8" cy="8" r="8" fill="#f70f1a"/><path d="M4.5 8.2l2.3 2.3 4.7-4.8" stroke="#fff" stroke-width="2" fill="none"/></svg>2 Car Garage</li>
        <li><svg viewBox="0 0 16 16"><circle cx="8" cy="8" r="8" fill="#f70f1a"/><path d="M4.5 8.2l2.3 2.3 4.7-4.8" stroke="#fff" stroke-width="2" fill="none"/></svg>3 Bed Room</li>
        <li><svg viewBox="0 0 16 16"><circle cx="8" cy="8" r="8" fill="#f70f1a"/><path d="M4.5 8.2l2.3 2.3 4.7-4.8" stroke="#fff" stroke-width="2" fill="none"/></svg>1 Dining Room</li>
        <li><svg viewBox="0 0 16 16"><circle cx="8" cy="8" r="8" fill="#f70f1a"/><path d="M4.5 8.2l2.3 2.3 4.7-4.8" stroke="#fff" stroke-width="2" fill="none"/></svg>1 Storage Room</li>
      </ul>
    </div>
  </section>

  <section class="gallery">
    <div class="gallery-frame"><div class="gallery-photo photo-modern" role="img" aria-label="Photograph of a modern dark multi-storey home with balconies"></div></div>
    <div class="gallery-frame"><div class="gallery-photo photo-blue" role="img" aria-label="Photograph of a blue two-storey house with a front lawn"></div></div>
    <div class="gallery-frame"><div class="gallery-photo photo-evening" role="img" aria-label="Photograph of a grey suburban house at dusk with garage"></div></div>
  </section>

  <p class="tagline">THE PERFECT HOME<span class="accent">TO SAVE THE FAMILY</span></p>
  <p class="tagline-body">Lorem Ipsum is simply dummy text of the printing and typesetting industry. Lorem Ipsum has been the industrysimply dummy text.</p>

  <footer>
    <div class="contact-call">
      <p class="call-label">Call For More Information</p>
      <p class="call-number"><svg viewBox="0 0 24 24"><path fill="#fff" d="M6.6 10.8a15 15 0 006.6 6.6l2.2-2.2c.3-.3.7-.4 1-.2 1.1.4 2.3.6 3.6.6.6 0 1 .4 1 1V20c0 .6-.4 1-1 1C10.6 21 3 13.4 3 4c0-.6.4-1 1-1h3.5c.6 0 1 .4 1 1 0 1.3.2 2.5.6 3.6.1.3 0 .7-.2 1z"/></svg>1800-555-014</p>
    </div>
    <div class="contact-details">
      <div class="contact-item"><svg viewBox="0 0 10 10"><path fill="#fff" d="M5 0a3.3 3.3 0 013.3 3.3C8.3 5.8 5 10 5 10S1.7 5.8 1.7 3.3A3.3 3.3 0 015 0zm0 2a1.3 1.3 0 100 2.6A1.3 1.3 0 005 2z"/></svg><span>Lorem Ipsum is simply dummy text<br>of the printing and text.</span></div>
      <span class="contact-sep"></span>
      <div class="contact-item"><svg viewBox="0 0 10 10"><circle cx="5" cy="5" r="4.3" fill="none" stroke="#fff" stroke-width="1"/><ellipse cx="5" cy="5" rx="1.8" ry="4.3" fill="none" stroke="#fff" stroke-width="0.8"/><path d="M0.7 5h8.6" stroke="#fff" stroke-width="0.8"/></svg><span>www.MarloweRealty.com</span></div>
      <span class="contact-sep"></span>
      <div class="contact-item"><svg viewBox="0 0 12 10"><rect x="0.5" y="1" width="11" height="8" fill="none" stroke="#fff"/><path d="M0.5 1l5.5 4.5L11.5 1" fill="none" stroke="#fff"/></svg><span>info@MarloweRealty.com</span></div>
    </div>
  </footer>
</main>
</body>
</html>
```